Website for solo law firm
Different areas of law
Hi PH
Changes done and updated.
Thanks
SolarPixelCrafter
Changes done and updated. Kindly check.
Star rating please...
Any Feedback?
Area of Service is primarily Personal Injury defense but it will be broaden to Immigration and Commercial law. At this time, the client is only concentrating in Personal Injury.
Hi tlumbrova ,
Please can you provide area of services?
The project has been VEILED. Please, those designers that have not posted, we are eager to see your designs before we start rating.
Thank you,
tlumbrova
Hello PH
Can you make the contest veiled?
Wex

```html
<!DOCTYPE html>
<html lang="en">
<head>
<meta charset="utf-8">
<title>The Law Office of Harlan T. Whitcombe</title>
<link rel="stylesheet" href="https://fonts.googleapis.com/css2?family=Arimo:wght@400;700&family=Tinos:wght@400;700&display=swap">
<style>
  :root {
    --brand-blue: #1d6fb8;
    --nav-top: #2a7cc4;
    --nav-bottom: #14589a;
    --link-blue: #3a8fd8;
    --text-dark: #222222;
    --text-muted: #9a9a9a;
    --rule: #c9c9c9;
    --footer: #a3a3a3;
    --hero-dark: #0e0c0a;
    --hero-warm: #3b2f24;
    --white: #ffffff;
  }
  * { margin: 0; padding: 0; box-sizing: border-box; }
  html, body { width: 1200px; height: 901px; overflow: hidden; background: var(--white); }
  body { position: relative; font-family: "Arimo", Arial, sans-serif; color: var(--text-dark); }

  .site-header { position: absolute; top: 0; left: 0; width: 1200px; height: 117px; }
  .brand { position: absolute; left: 70px; top: 22px; display: flex; align-items: center; gap: 12px; }
  .brand-mark { width: 52px; height: 52px; border-radius: 50%; background: var(--brand-blue); }
  .brand-name { font-family: "Tinos", serif; font-size: 24px; font-weight: 400; color: var(--brand-blue); line-height: 1.1; }
  .search { position: absolute; left: 1005px; top: 49px; width: 145px; height: 24px; background: #b9b9b9; color: var(--white);
            font-size: 11px; letter-spacing: 1px; padding: 6px 8px; }
  .social { position: absolute; left: 1008px; top: 78px; display: flex; gap: 6px; }
  .social span { width: 16px; height: 16px; background: #b0b0b0; border-radius: 2px; }

  .main-nav { position: absolute; top: 117px; left: 0; width: 1200px; height: 34px;
              background: linear-gradient(var(--nav-top), var(--nav-bottom)); }
  .main-nav a { position: absolute; top: 6px; font-family: "Tinos", serif; font-weight: 700; font-size: 19px;
                color: var(--white); text-decoration: none; transform: translateX(-50%); white-space: nowrap; }

  .hero { position: absolute; top: 151px; left: 0; width: 1200px; height: 331px;
          background: linear-gradient(90deg, var(--hero-dark) 0%, #1d1812 35%, var(--hero-warm) 70%, #4a3c2e 85%, #241c15 100%); }
  .hero-copy { position: absolute; left: 202px; top: 88px; width: 560px; }
  .hero-title { font-size: 28px; font-weight: 700; color: var(--link-blue); margin-bottom: 6px; }
  .hero-text { font-size: 16px; font-weight: 700; line-height: 21px; color: var(--white); }
  .hero-text a { color: var(--link-blue); text-decoration: none; }
  .hero-rule { width: 200px; height: 2px; background: var(--link-blue); margin-top: 6px; }

  .column { position: absolute; top: 528px; }
  .column-title { font-size: 21px; line-height: 24px; color: var(--brand-blue); font-weight: 400; }
  .column-rule { height: 1px; background: var(--rule); margin: 4px 0 6px; }
  .column-text { font-size: 12.5px; line-height: 15px; color: var(--text-dark); }
  .col-cases { left: 117px; width: 345px; }
  .col-reviews { left: 530px; width: 345px; }

  .contact { position: absolute; left: 935px; top: 528px; width: 209px; }
  .contact .column-title { margin-bottom: 4px; }
  .field-label { font-size: 12px; color: var(--text-muted); margin-top: 6px; }
  .field { height: 20px; border: 1px solid #c2c2c2; margin-top: 3px; }
  .submit { display: inline-block; margin-top: 8px; font-size: 11px; font-weight: 700; color: var(--brand-blue); }
  .address { position: absolute; left: 935px; top: 774px; font-size: 10.5px; line-height: 13.5px; color: var(--brand-blue); }

  .site-footer { position: absolute; left: 0; top: 852px; width: 1200px; height: 49px; background: var(--footer);
                 font-family: "Tinos", serif; font-weight: 700; font-size: 15px; color: var(--white); }
  .footer-links { position: absolute; left: 49px; top: 15px; }
  .copyright { position: absolute; right: 37px; top: 15px; }
</style>
</head>
<body>
  <header class="site-header">
    <div class="brand">
      <span class="brand-mark"></span>
      <span class="brand-name">Harlan T. Whitcombe</span>
    </div>
    <div class="search">SEARCH</div>
    <div class="social"><span></span><span></span><span></span></div>
  </header>

  <nav class="main-nav">
    <a style="left:285px">Home</a>
    <a style="left:397px">About Us</a>
    <a style="left:528px">Practices</a>
    <a style="left:638px">News</a>
    <a style="left:755px">Experience</a>
    <a style="left:900px">Contact Us</a>
  </nav>

  <section class="hero" role="img" aria-label="Photograph of a law library aisle with shelves of bound books">
    <div class="hero-copy">
      <h1 class="hero-title">Lorem ipsum</h1>
      <p class="hero-text">Lorem ipsum dolor sit amet, consectetuer adipiscing elit, sed diam nonummy nibh euismod tincidunt ut laoreet dolore magna aliquam erat volutpat. Ut wisi enim ad minim veniam, quis nostrud exerci tation ullamcorper suscipit lobortis nisl ut aliquip ex ea commodo consequat. <a>read more...</a></p>
      <div class="hero-rule"></div>
    </div>
  </section>

  <section class="column col-cases">
    <h2 class="column-title">Case<br>Examples &amp; Results</h2>
    <div class="column-rule"></div>
    <p class="column-text">Lorem ipsum dolor sit amet, consectetuer adipiscing elit, sed diam nonummy nibh euismod tincidunt ut laoreet dolore magna aliquam erat volutpat.<br>Ut wisi enim ad minim veniam, quis nostrud exerci tation ullamcorper suscipit lobortis nisl ut aliquip ex ea commodo consequat.<br>Duis autem vel eum iriure dolor in hendrerit in vulputate velit esse molestie consequat, vel illum dolore eu feugiat nulla facilisis at vero eros et accumsan et iusto odio dignissim qui blandit praesent luptatum zzril delenit augue duis dolore te feugait nulla facilisi. Nam liber tempor cum soluta nobis eleifend option congue nihil imperdiet doming id quod mazim placerat facer possim assum.</p>
  </section>

  <section class="column col-reviews">
    <h2 class="column-title">Client<br>Reviews &amp; Ratings</h2>
    <div class="column-rule"></div>
    <p class="column-text">Lorem ipsum dolor sit amet, consectetuer adipiscing elit, sed diam nonummy nibh euismod tincidunt ut laoreet dolore magna aliquam erat volutpat.<br>Ut wisi enim ad minim veniam, quis nostrud exerci tation ullamcorper suscipit lobortis nisl ut aliquip ex ea commodo consequat.<br>Duis autem vel eum iriure dolor in hendrerit in vulputate velit esse molestie consequat, vel illum dolore eu feugiat nulla facilisis at vero eros et accumsan et iusto odio dignissim qui blandit praesent luptatum zzril delenit augue duis dolore te feugait nulla facilisi. Nam liber tempor cum soluta nobis eleifend option congue nihil imperdiet doming id quod mazim placerat facer possim assum.</p>
  </section>

  <aside class="contact">
    <h2 class="column-title">Contact Us</h2>
    <div class="column-rule"></div>
    <div class="field-label">Name</div><div class="field"></div>
    <div class="field-label">Email</div><div class="field"></div>
    <div class="field-label">Phone</div><div class="field"></div>
    <div class="field-label">Question</div><div class="field"></div>
    <span class="submit">Submit »</span>
  </aside>

  <address class="address" style="font-style:normal">
    2480 W. Harbor Lane<br>
    Suite #210<br>
    Lakeview, FL 30418<br>
    Tel: 954-555-0142<br>
    Fax: 954-555-0178<br>
    info@whitcombelaw.example
  </address>

  <footer class="site-footer">
    <div class="footer-links">Site Map | Privacy Policy | Contact Us | Terms and Conditions</div>
    <div class="copyright">Copyright © 2013 Whitcombe Law. All rights reserved.</div>
  </footer>
</body>
</html>
```